The Brightpath Scholar, an online college fair for non-traditional students, needs a web site

I need design and coding for a functioning web site that will serve as an online college fair that connects non-traditional students with college admissions officers and college advisors. I have chosen Wordpress and the "Meridian" theme for the site, and you can see what I already have here: https://brightpathscholar.example/
I need help setting up the site's pages and functionality, including SEO optimization and a password protected area. I will manage all content. In addition to me as the administrator, other users will be: college admissions officers, non-traditional students (like homeschoolers), and college advisors.
Target Market(s)
Homeschoolers and college/university admissions officers
Industry/Entity Type
College
Coding
Coded - Design and coding required
Number of Pages Required
5+ page
Requirements
Must have
- - An inviting but professional look (see the logo as a starting point)
- - Easy to navigate
- - A way to register subscribed members (students)
- - A password-protected "members only" area
- - Virtual "booths" on the Schools page that lead to a detail page for each school
- - SEO optimized
Nice to have
- - Searchable site

```html
<!DOCTYPE html>
<html lang="en">
<head>
<meta charset="utf-8">
<title>The Brightpath Scholar – A Virtual College For Non-Traditional Students</title>
<link rel="stylesheet" href="https://fonts.googleapis.com/css2?family=Open+Sans:wght@400;600;700;800&display=swap">
<style>
:root{
  --red:#e8141b;
  --lavender:#c4a8f7;
  --ink:#1b1b1b;
  --muted:#444;
  --page:#fbf9fb;
  --white:#ffffff;
  --line:#8a8a8a;
  --footer:#000000;
}
*{box-sizing:border-box;margin:0;padding:0}
html,body{width:1200px;height:3422px;overflow:hidden}
body{position:relative;background:var(--page);font-family:"Open Sans",Arial,sans-serif;color:var(--ink)}
a{color:inherit;text-decoration:none}
.abs{position:absolute}

/* top bar */
.topbar{left:0;top:0;width:1200px;height:30px;background:var(--white);font-size:12px}
.topbar .tagline{left:86px;top:7px;display:flex;align-items:center;gap:8px}
.topbar .account{right:86px;top:7px}

/* navigation */
.mainnav{left:0;top:30px;width:1200px;height:73px;background:var(--lavender)}
.mainnav ul{position:absolute;right:128px;top:27px;display:flex;gap:18px;list-style:none;font-size:14px;color:#222}

/* hero */
.hero{left:0;top:103px;width:1200px;height:559px;overflow:hidden;
  background:linear-gradient(90deg,#3a4250 0%,#6d737c 35%,#8b8784 60%,#b49a8c 80%,#7e7a78 100%)}
.hero .shade{inset:0;background:rgba(20,20,30,.25)}
.brand{left:96px;top:20px;display:flex;align-items:center;gap:18px;color:var(--white)}
.brand .mark{width:60px;height:60px;background:var(--red)}
.brand .name{font-size:30px;font-weight:600;line-height:1.05;letter-spacing:.5px}
.brand .sub{font-size:15px;font-weight:400;margin-top:4px}
.hero-copy{left:0;top:236px;width:1208px;text-align:center;color:var(--white);text-shadow:0 2px 6px rgba(0,0,0,.45)}
.hero-copy h1{font-size:58px;font-weight:700;letter-spacing:1px;line-height:1}
.hero-copy h2{font-size:27px;font-weight:700;margin-top:14px}
.hero-copy p{font-size:19px;margin-top:4px}
.btn-outline{left:529px;top:451px;width:148px;height:48px;border:2px solid var(--red);color:var(--white);
  font-size:16px;font-weight:700;display:flex;align-items:center;justify-content:center;background:rgba(0,0,0,.15)}

/* section titles */
.section-title{left:0;width:1200px;text-align:center;font-size:33px;font-weight:600;letter-spacing:.5px}

/* how it works */
.step{width:380px;text-align:center}
.step .icon{height:78px;display:flex;align-items:flex-end;justify-content:center}
.step h3{font-size:17px;font-weight:400;margin-top:12px}
.step p{font-size:13px;line-height:1.4;margin-top:14px;color:var(--muted)}

/* advisors */
.advisor{top:1113px;width:338px;height:435px;background:var(--white);border:1px solid var(--line)}
.advisor .photo{left:0;top:0;width:100%;height:294px}
.advisor .name{left:0;top:304px;width:100%;text-align:center;font-size:16px}
.advisor .course{left:0;top:344px;width:100%;text-align:center;font-size:16px;font-weight:600;line-height:1.35}
.advisor .bar{left:50%;bottom:-4px;width:106px;height:8px;margin-left:-53px;background:var(--red);border-radius:4px}

/* featured school */
.school{left:84px;top:1711px;width:1029px;height:381px;
  background:linear-gradient(135deg,#3c3a44 0%,#6a5a58 40%,#8b7868 70%,#4d4a52 100%)}
.school p{position:absolute;left:128px;top:112px;width:774px;text-align:center;color:var(--white);
  font-size:16px;line-height:1.22;text-shadow:0 1px 3px rgba(0,0,0,.7)}

/* news */
.news{width:506px;height:297px;background:var(--white);border:1px solid var(--line)}
.news .photo{left:0;top:0;width:262px;height:100%}
.news .body{left:262px;top:0;width:243px;height:100%;text-align:center}
.news .date{position:absolute;left:78px;top:10px;display:flex;align-items:baseline;gap:8px}
.news .date small{font-size:14px}
.news .date strong{font-size:33px;font-weight:600}
.news .meta{position:absolute;left:0;top:80px;width:100%;font-size:11.5px}
.news .excerpt{position:absolute;left:30px;top:104px;width:183px;font-size:11.5px;line-height:1.55}
.btn-red{position:absolute;top:185px;left:69px;width:104px;height:30px;background:var(--red);color:var(--white);
  font-size:11px;font-weight:600;display:flex;align-items:center;justify-content:center}

/* newsletter */
.newsletter-title{left:0;top:2910px;width:1200px;text-align:center;font-size:30px;font-weight:600;line-height:1.25}
.subscribe{left:290px;top:3027px;width:625px;height:53px;border:2px solid #555;border-radius:27px;overflow:hidden;background:var(--white)}
.subscribe span{position:absolute;left:22px;top:16px;font-size:12px;color:#333}
.subscribe button{position:absolute;right:0;top:0;width:151px;height:100%;border:0;background:var(--red);
  color:#111;font-family:inherit;font-size:12px;font-weight:600}

/* footer */
.footer{left:0;top:3123px;width:1200px;height:299px;background:var(--footer);color:var(--white)}
.footer h4{font-size:14px;font-weight:700;margin-bottom:14px}
.footer .col{top:52px;font-size:12.5px;line-height:1.33}
.footer ul{list-style:none}
.social li{display:flex;align-items:center;gap:8px;margin-bottom:9px}
.social .dot{width:12px;height:12px;border-radius:50%;background:var(--white)}
.footer .copy{left:86px;bottom:20px;font-size:12.5px}
</style>
</head>
<body>

<header>
  <div class="abs topbar">
    <div class="abs tagline">
      <svg width="18" height="12" viewBox="0 0 18 12" aria-hidden="true"><path d="M9 0 18 4 9 8 0 4Z M4 6v3c3 2 7 2 10 0V6L9 8Z" fill="#111"/></svg>
      <span>Best learning management template for ever</span>
    </div>
    <div class="abs account"><a href="#">Login</a> &nbsp;|&nbsp; <a href="#">Register</a></div>
  </div>

  <nav class="abs mainnav">
    <ul>
      <li>HOME</li><li>STUDENTS</li><li>SCHOOL</li><li>ADVISORS</li><li>MEMBER RESOURCES</li><li>NEWS</li><li>CONTACT US</li>
    </ul>
  </nav>

  <section class="abs hero">
    <div class="abs" role="img" aria-label="Smiling student seated in a classroom with classmates blurred behind" style="inset:0"></div>
    <div class="abs shade"></div>
    <div class="abs brand">
      <div class="mark"></div>
      <div>
        <div class="name">THE BRIGHTPATH SCHOLAR</div>
        <div class="sub">A Virtual College For Non-Traditional Students</div>
      </div>
    </div>
    <div class="abs hero-copy">
      <h1>MEET NEW FRIENDS</h1>
      <h2>AND STUDY WITH EXPERTS</h2>
      <p>We Belive There Is Nothing More Important Than Education.</p>
    </div>
    <a class="abs btn-outline" href="#">READ MORE</a>
  </section>
</header>

<main>
  <h2 class="abs section-title" style="top:700px">HOW IT WORKS</h2>

  <div class="abs step" style="left:84px;top:784px">
    <div class="icon">
      <svg width="110" height="72" viewBox="0 0 110 72" aria-hidden="true">
        <path d="M55 4 108 24 55 44 2 24Z" fill="#111"/>
        <path d="M24 34v22c18 12 44 12 62 0V34L55 46Z" fill="#111"/>
        <path d="M98 28v24" stroke="#111" stroke-width="3"/><circle cx="98" cy="54" r="4" fill="#111"/>
      </svg>
    </div>
    <h3>Multi-Tier Courses</h3>
    <p>Lorem ipsum dolor sit amet, consectetur adipi-<br>ing elit. Integer loectetur adipiling elit. Integer<br>lectetur adipiling elit. Integer lrem quam..</p>
  </div>

  <div class="abs step" style="left:408px;top:784px">
    <div class="icon">
      <svg width="96" height="70" viewBox="0 0 96 70" aria-hidden="true" fill="none" stroke="#111" stroke-width="3">
        <rect x="32" y="4" width="32" height="18" rx="3"/>
        <rect x="6" y="14" width="18" height="12" rx="3"/><rect x="72" y="14" width="18" height="12" rx="3"/>
        <circle cx="18" cy="36" r="5" fill="#111"/><circle cx="78" cy="36" r="5" fill="#111"/>
        <circle cx="48" cy="34" r="5" fill="#111"/>
        <path d="M10 66V48h16v18M70 66V48h16v18M40 50h16"/>
        <path d="M30 52h36M36 52v14M60 52v14"/>
      </svg>
    </div>
    <h3>College</h3>
    <p>Lorem ipsum dolor sit amet, consectetur adipiling<br>elit. Integer loectetur adipiling elit. Integer lectetur<br>adipiling elit. Integer lrem quam..</p>
  </div>

  <div class="abs step" style="left:768px;top:784px">
    <div class="icon"><span style="font-size:82px;font-weight:800;line-height:.9">?</span></div>
    <h3>Advanced Quizzing</h3>
    <p>Lorem ipsum dolor sit amet, consectetur adipi-<br>ing elit. Integer loectetur adipiling elit. Integer<br>lectetur adipiling elit. Integer lrem quam..</p>
  </div>

  <h2 class="abs section-title" style="top:1030px">FEATURED ADVISORS</h2>

  <article class="abs advisor" style="left:84px">
    <div class="abs photo" role="img" aria-label="Portrait of advisor in a grey blazer" style="background:linear-gradient(180deg,#f4f2f1,#d8d0cc)"></div>
    <div class="abs name">Mara Ellison</div>
    <div class="abs course">Introduction Lessonforge-<br>LMS plugin</div>
    <div class="abs bar"></div>
  </article>
  <article class="abs advisor" style="left:433px">
    <div class="abs photo" role="img" aria-label="Portrait of advisor in shirt and tie" style="background:linear-gradient(180deg,#f6f6f7,#c8d4e4)"></div>
    <div class="abs name">Jonah Fielding</div>
    <div class="abs course">From Zero to Hero with<br>Nodewick</div>
    <div class="abs bar"></div>
  </article>
  <article class="abs advisor" style="left:778px">
    <div class="abs photo" role="img" aria-label="Portrait of advisor seated in an office" style="background:linear-gradient(180deg,#dfe3e6,#8d97a3)"></div>
    <div class="abs name">Owen Marsh</div>
    <div class="abs course">Learn Serpentel - Interactive<br>Serpentel</div>
    <div class="abs bar"></div>
  </article>

  <h2 class="abs section-title" style="top:1607px">FEATURED SCHOOL</h2>

  <section class="abs school" role="img" aria-label="Classroom of young students playing xylophones with hands raised">
    <p>There are many variations of passages of Lorem Ipsum available, but the majority have suffered alteration in some form, by injected humour, or randomised words which don't look even slightly believable. If you are going to use a passage of Lorem Ipsum, you need to be sure there isn't anything embarrassing hidden in the middle of text. All the Lorem Ipsum generators on the Internet tend to repeat predefined chunks as necessary, making this the first true generator on the Internet. It uses a dictionary of over 200 Latin words, combined with a handful of model sentence structures, to generate Lorem Ipsum which looks reasonable. The generated Lorem Ipsum is therefore always free from repetition, injected humour, or non-characteristic words etc.</p>
  </section>

  <h2 class="abs section-title" style="top:2152px">LATEST NEWS</h2>

  <article class="abs news" style="left:84px;top:2263px">
    <div class="abs photo" role="img" aria-label="Two students studying together at a desk" style="background:linear-gradient(135deg,#3b4a66,#c9b6a6)"></div>
    <div class="abs body">
      <div class="date"><small>JUN</small><strong>25</strong></div>
      <div class="meta">25 Jun 2050 59 19</div>
      <p class="excerpt">There are many variaons of passages of Lorem Ipsuable, amrn in some by injected humour,</p>
      <a class="btn-red" href="#">LEARN NOW</a>
    </div>
  </article>
  <article class="abs news" style="left:604px;top:2263px">
    <div class="abs photo" role="img" aria-label="Teacher helping a student at a desk" style="background:linear-gradient(135deg,#6f7580,#c8c2bc)"></div>
    <div class="abs body">
      <div class="date"><small>JUN</small><strong>28</strong></div>
      <div class="meta">25 Jun 2050 59 19</div>
      <p class="excerpt">There are many variaons of passages of Lorem Ipsuable, amrn in some by injected humour,</p>
      <a class="btn-red" href="#">LEARN NOW</a>
    </div>
  </article>
  <article class="abs news" style="left:84px;top:2578px">
    <div class="abs photo" role="img" aria-label="Group of students and a mentor around a computer" style="background:linear-gradient(135deg,#a06a5a,#e2d8d0)"></div>
    <div class="abs body">
      <div class="date"><small>JUN</small><strong>26</strong></div>
      <div class="meta">25 Jun 2050 59 19</div>
      <p class="excerpt">There are many variaons of passages of Lorem Ipsuable, amrn in some by injected humour,</p>
      <a class="btn-red" href="#">LEARN NOW</a>
    </div>
  </article>
  <article class="abs news" style="left:604px;top:2578px">
    <div class="abs photo" role="img" aria-label="Smiling student in uniform in a classroom" style="background:linear-gradient(135deg,#4a3a36,#b8aaa6)"></div>
    <div class="abs body">
      <div class="date"><small>JUN</small><strong>15</strong></div>
      <div class="meta">25 Jun 2050 59 19</div>
      <p class="excerpt">There are many variaons of passages of Lorem Ipsuable, amrn in some by injected humour,</p>
      <a class="btn-red" href="#">LEARN NOW</a>
    </div>
  </article>

  <h2 class="abs newsletter-title">SUBSCRIBE<br>TO OUR NEWSLETTER</h2>
  <form class="abs subscribe">
    <span>Enter your email address</span>
    <button type="button">SUBSCRIBE</button>
  </form>
</main>

<footer class="abs footer">
  <div class="abs col" style="left:128px">
    <h4>QUICK MENU</h4>
    <ul><li>HOME</li><li>STUDENTS</li><li>SCHOOL</li><li>ADVISORS</li><li>MEMBER RESORCES</li><li>NEWS</li><li>CONTACT US</li></ul>
  </div>
  <div class="abs col" style="left:354px;width:270px">
    <h4>ABOUT US</h4>
    <p>UT ANTE EST, FACILISIS EU ODIO SIT VIVERRA MI, PELLENT NDUM NIST VITAE ROIN TINCIDUNT NEQUE EGET</p>
  </div>
  <div class="abs col" style="left:750px">
    <h4>FOLLOW US</h4>
    <ul class="social">
      <li><span class="dot"></span>WORKWEAVE</li>
      <li><span class="dot"></span>FRIENDLOOM</li>
      <li><span class="dot"></span>PHOTOQUILL</li>
      <li><span class="dot"></span>PLUSORBIT</li>
    </ul>
  </div>
  <div class="abs col" style="left:926px">
    <h4>CONNECT WITH US</h4>
    <p>LOG IN <span style="margin-left:58px">SIGN UP</span></p>
  </div>
  <div class="abs copy">COPYRIGHT BRIGHTPATH2017. ALL RIGHT RESEVAD</div>
</footer>

</body>
</html>
```